Branding website for a Data Science company with 1 product

Branding website for a Data Science company, featuring our main product: Lumoria. The purpose of the website is to get potential clients to get a peek at what we do, but the main purpose is to get them to get in touch with us. The website will not answer all questions. Therefore the contact details and contact form is a must-have .

Target Market(s)

Potential new B2B clients with medium to large websites, application users (behind a login)

Industry/Entity Type

It Company

Coding

Coded - Design and coding required

Number of Pages Required

2 page

Font styles to use
Sans Serif

Colors

Designer to choose colors to be used in the design.

Requirements
Must have
• A contact form and branding a product

```html
<!DOCTYPE html>
<html lang="en">
<head>
<meta charset="utf-8">
<title>Kestrel Partners</title>
<link rel="stylesheet" href="https://fonts.googleapis.com/css2?family=Roboto:wght@300;400;500;700&family=Open+Sans:wght@400;600&display=swap">
<style>
:root{
  --orange:#f05a22;
  --orange-soft:rgba(240,90,34,.88);
  --ink:#333333;
  --muted:#555555;
  --grey:#666666;
  --light:#f2f2f2;
  --white:#ffffff;
  --footer:#efefef;
}
*{box-sizing:border-box;margin:0;padding:0}
html,body{width:1200px;height:2980px;overflow:hidden}
body{font-family:"Open Sans",sans-serif;color:var(--ink);background:var(--white);position:relative}
.abs{position:absolute}
h1,h2,h3{font-family:"Roboto",sans-serif}

/* hero */
.hero{left:0;top:0;width:1200px;height:530px;background:linear-gradient(180deg,#3c4650 0%,#5a5852 45%,#3a3632 100%)}
.hero-title{left:0;width:1200px;top:200px;text-align:center;color:var(--white);font-size:62px;font-weight:700;letter-spacing:1px}
.hero-sub{left:0;width:1200px;top:290px;text-align:center;color:var(--white);font-size:17px}

/* nav */
.nav{left:0;top:530px;width:1200px;height:76px;background:var(--light)}
.brand{left:110px;top:24px;display:flex;align-items:center;gap:10px}
.brand-dot{width:26px;height:26px;border-radius:50%;background:var(--orange)}
.brand-name{font-family:"Roboto",sans-serif;font-weight:500;font-size:19px;color:var(--ink);letter-spacing:1px;line-height:26px;white-space:nowrap}
.menu{left:412px;top:24px;display:flex;list-style:none;font-family:"Roboto",sans-serif;font-size:11px;font-weight:500;color:var(--ink)}
.menu li{padding:8px 12px;margin-right:4px}
.menu li.active{background:var(--orange);color:var(--white)}
.flags{left:1020px;top:26px;display:flex;gap:16px}

/* services */
.services{left:0;top:606px;width:1200px;height:529px;background:linear-gradient(120deg,#b24a26,#e0692f 50%,#c45a30)}
.services-overlay{left:0;top:606px;width:1200px;height:529px;background:var(--orange-soft)}
.section-title{left:0;width:1200px;text-align:center;font-size:36px;font-weight:700}
.section-sub{left:0;width:1200px;text-align:center;font-size:16px}
.feature{width:240px;text-align:center}
.ring{width:108px;height:108px;border-radius:50%;margin:0 auto;display:flex;align-items:center;justify-content:center}
.ring-light{border:2px solid var(--white)}
.ring-orange{border:2px solid var(--orange)}
.feature h3{font-size:19px;font-weight:500;margin-top:30px}
.feature p{font-size:13px;line-height:20px;margin:14px auto 0;width:196px}
.on-orange{color:var(--white)}

/* what we do */
.intro{left:360px;width:480px;top:1262px;text-align:center;font-size:12.5px;line-height:21px;color:var(--muted)}
.more{margin-top:14px;font-size:11px;color:var(--orange);display:flex;justify-content:center;align-items:center;gap:8px}

/* products */
.products{left:0;top:1664px;width:1200px;height:418px;background:linear-gradient(180deg,#4a4d50,#5e5c58 60%,#3f4a4c)}
.products-overlay{left:0;top:1664px;width:1200px;height:418px;background:rgba(30,30,30,.55)}
.product-intro{left:370px;width:460px;top:1790px;text-align:center;color:var(--white);font-size:12.5px;line-height:21px}
.checks{list-style:none;color:var(--white);font-size:11.5px}
.checks li{height:31px;display:flex;align-items:center;gap:12px}
.btn-ghost{left:512px;top:1982px;width:178px;height:44px;border:2px solid var(--white);color:var(--white);font-family:"Roboto",sans-serif;font-size:13px;display:flex;align-items:center;justify-content:center}

/* contact */
.contact{left:0;top:2082px;width:1200px;height:374px;background:var(--orange)}
.field{background:var(--white);height:36px;font-size:10px;color:#9a9a9a;padding:12px 14px;letter-spacing:.5px}
.btn-submit{left:456px;top:2370px;width:290px;height:36px;border:2px solid var(--white);color:var(--white);font-family:"Roboto",sans-serif;font-weight:700;font-size:13px;display:flex;align-items:center;justify-content:center}

/* map */
.map{left:0;top:2456px;width:1200px;height:212px;background:linear-gradient(90deg,#dfe6d8,#ece7de 45%,#b9d2ec 75%,#e4e8dc)}

/* footer */
.footer{left:0;top:2668px;width:1200px;height:312px;background:var(--footer)}
.foot-head{font-family:"Roboto",sans-serif;font-weight:400;font-size:17px;color:var(--grey);top:2742px}
.foot-list{list-style:none;font-size:11px;color:var(--ink);top:2782px}
.foot-list li{height:20.5px;display:flex;align-items:center;gap:12px}
.bullet{width:0;height:0;border-left:5px solid var(--orange);border-top:3px solid transparent;border-bottom:3px solid transparent}
.contact-line{height:30px !important}
.orange-text{color:var(--orange)}
.foot-about{left:816px;top:2800px;width:290px;font-size:11.5px;line-height:19px;color:var(--ink)}
.copyright{left:816px;top:2878px;font-size:11px;color:var(--orange)}
.social-dot{width:16px;height:16px;border-radius:50%;border:1.5px solid var(--grey)}
</style>
</head>
<body>

<!-- hero -->
<div class="abs hero" role="img" aria-label="Evening panorama of a city skyline with rooftops and a square"></div>
<h1 class="abs hero-title">KESTREL PARTNERS</h1>
<p class="abs hero-sub">The right message at the right time to the right customer</p>

<!-- navigation -->
<header class="abs nav">
  <div class="abs brand">
    <span class="brand-dot"></span>
    <span class="brand-name">KESTREL PARTNERS</span>
  </div>
  <ul class="abs menu">
    <li class="active">HOME</li><li>ABOUT US</li><li>SERVICES</li><li>PROFILES</li><li>TIPS &amp; LINKS</li><li>CLIENT LOGIN</li><li>CONTACT</li>
  </ul>
  <div class="abs flags">
    <svg width="28" height="20" viewBox="0 0 28 20"><rect width="28" height="7" fill="#ae1c28"/><rect y="7" width="28" height="6" fill="#fff"/><rect y="13" width="28" height="7" fill="#21468b"/></svg>
    <svg width="28" height="20" viewBox="0 0 28 20"><rect width="28" height="20" fill="#012169"/><path d="M0 0L28 20M28 0L0 20" stroke="#fff" stroke-width="4"/><path d="M14 0V20M0 10H28" stroke="#fff" stroke-width="6"/><path d="M14 0V20M0 10H28" stroke="#c8102e" stroke-width="3"/></svg>
  </div>
</header>

<!-- services -->
<section>
  <div class="abs services" role="img" aria-label="Photo of colleagues working together at a table"></div>
  <div class="abs services-overlay"></div>
  <h2 class="abs section-title on-orange" style="top:672px">SERVICES</h2>
  <p class="abs section-sub on-orange" style="top:728px">Love My Work?</p>

  <div class="abs feature on-orange" style="left:120px;top:796px">
    <div class="ring ring-light"><svg width="40" height="36" viewBox="0 0 40 36" fill="#fff"><rect x="2" y="9" width="36" height="25" rx="3"/><rect x="14" y="3" width="12" height="8" rx="2" fill="none" stroke="#fff" stroke-width="3"/><rect x="17" y="18" width="6" height="5" fill="#f05a22"/></svg></div>
    <h3>WEB DESIGN</h3><p>Deinde disputat, quod cuiusque generis animantium statui deceat extremum. Sed vobis voluptatum</p>
  </div>
  <div class="abs feature on-orange" style="left:358px;top:796px">
    <div class="ring ring-light"><svg width="34" height="42" viewBox="0 0 34 42" fill="#fff"><path d="M4 8L30 2V40H4Z"/><g fill="#f05a22"><rect x="10" y="12" width="14" height="3"/><rect x="10" y="19" width="14" height="3"/><rect x="10" y="26" width="14" height="3"/></g></svg></div>
    <h3>WEB DESIGN</h3><p>Deinde disputat, quod cuiusque generis animantium statui deceat extremum. Sed vobis voluptatum</p>
  </div>
  <div class="abs feature on-orange" style="left:598px;top:796px">
    <div class="ring ring-light"><svg width="50" height="32" viewBox="0 0 50 32" fill="#fff"><path d="M2 8L12 4L25 12L38 4L48 8V20L36 26L28 30L22 26L14 24L2 18Z"/><path d="M16 14L26 22M22 12L32 20" stroke="#f05a22" stroke-width="2.5"/></svg></div>
    <h3>WEB DESIGN</h3><p>Deinde disputat, quod cuiusque generis animantium statui deceat extremum. Sed vobis voluptatum</p>
  </div>
  <div class="abs feature on-orange" style="left:836px;top:796px">
    <div class="ring ring-light"><svg width="34" height="42" viewBox="0 0 34 42" fill="#fff"><path d="M4 8L30 2V40H4Z"/><g fill="#f05a22"><rect x="10" y="12" width="14" height="3"/><rect x="10" y="19" width="14" height="3"/><rect x="10" y="26" width="14" height="3"/></g></svg></div>
    <h3>WEB DESIGN</h3><p>Deinde disputat, quod cuiusque generis animantium statui deceat extremum. Sed vobis voluptatum</p>
  </div>
</section>

<!-- what we do -->
<section>
  <h2 class="abs section-title" style="top:1194px;color:var(--orange)">WHAT WE DO</h2>
  <p class="abs intro">Deinde disputat, quod cuiusque generis animantium statui deceat extremum. Sed vobis voluptatum perceptarum recordatio vitam beatam facit, et quidem</p>

  <div class="abs feature" style="left:162px;top:1344px">
    <div class="ring ring-orange"><svg width="40" height="42" viewBox="0 0 40 42" fill="none" stroke="#f05a22" stroke-width="2.5"><rect x="4" y="6" width="26" height="32"/><path d="M10 14H24M10 20H24M10 26H18"/><path d="M24 30L36 12L38 14L26 32Z" fill="#f05a22"/></svg></div>
    <h3 style="color:var(--orange)">INSIGHTS</h3><p style="color:var(--muted)">Deinde disputat, quod cuiusque generis animantium</p>
    <div class="more"><svg width="18" height="10" viewBox="0 0 18 10"><rect x="1" y="1" width="16" height="8" fill="none" stroke="#f05a22" stroke-width="1.5"/><path d="M4 5H14" stroke="#f05a22" stroke-width="1.5"/></svg>Read More</div>
  </div>
  <div class="abs feature" style="left:482px;top:1344px">
    <div class="ring ring-orange"><svg width="44" height="32" viewBox="0 0 44 32" fill="none" stroke="#f05a22" stroke-width="2.5"><rect x="3" y="3" width="38" height="26"/><path d="M3 3L22 18L41 3"/></svg></div>
    <h3 style="color:var(--orange)">ADVISORY</h3><p style="color:var(--muted)">Deinde disputat, quod cuiusque generis animantium</p>
    <div class="more"><svg width="18" height="10" viewBox="0 0 18 10"><rect x="1" y="1" width="16" height="8" fill="none" stroke="#f05a22" stroke-width="1.5"/><path d="M4 5H14" stroke="#f05a22" stroke-width="1.5"/></svg>Read More</div>
  </div>
  <div class="abs feature" style="left:798px;top:1344px">
    <div class="ring ring-orange"><svg width="50" height="32" viewBox="0 0 50 32" fill="none" stroke="#f05a22" stroke-width="2.5"><path d="M2 8L12 4L25 12L38 4L48 8V20L36 26L28 30L22 26L14 24L2 18Z"/><path d="M16 14L26 22M22 12L32 20"/></svg></div>
    <h3 style="color:var(--orange)">SECURITY</h3><p style="color:var(--muted)">Deinde disputat, quod cuiusque generis animantium</p>
    <div class="more"><svg width="18" height="10" viewBox="0 0 18 10"><rect x="1" y="1" width="16" height="8" fill="none" stroke="#f05a22" stroke-width="1.5"/><path d="M4 5H14" stroke="#f05a22" stroke-width="1.5"/></svg>Read More</div>
  </div>
</section>

<!-- products -->
<section>
  <div class="abs products" role="img" aria-label="Photo of a canal lined with tall townhouses and a bridge"></div>
  <div class="abs products-overlay"></div>
  <h2 class="abs section-title" style="top:1724px;color:var(--white)">OUR PRODUCTS</h2>
  <p class="abs product-intro">Lumoria is our on-demand, software-as-a-service real-time streaming data platform. You can use it to capture, analyze, profile and target your customers.</p>
  <ul class="abs checks" style="left:278px;top:1843px">
    <li><svg width="14" height="14" viewBox="0 0 14 14"><circle cx="7" cy="7" r="7" fill="#f05a22"/><path d="M3.5 7L6 9.5L10.5 4.5" stroke="#fff" stroke-width="1.8" fill="none"/></svg>Works on your own database</li>
    <li><svg width="14" height="14" viewBox="0 0 14 14"><circle cx="7" cy="7" r="7" fill="#f05a22"/><path d="M3.5 7L6 9.5L10.5 4.5" stroke="#fff" stroke-width="1.8" fill="none"/></svg>Real-time website visitor tracking</li>
    <li><svg width="14" height="14" viewBox="0 0 14 14"><circle cx="7" cy="7" r="7" fill="#f05a22"/><path d="M3.5 7L6 9.5L10.5 4.5" stroke="#fff" stroke-width="1.8" fill="none"/></svg>Real-time profiling</li>
    <li><svg width="14" height="14" viewBox="0 0 14 14"><circle cx="7" cy="7" r="7" fill="#f05a22"/><path d="M3.5 7L6 9.5L10.5 4.5" stroke="#fff" stroke-width="1.8" fill="none"/></svg>Real-time recommendations</li>
  </ul>
  <ul class="abs checks" style="left:572px;top:1843px">
    <li><svg width="14" height="14" viewBox="0 0 14 14"><circle cx="7" cy="7" r="7" fill="#f05a22"/><path d="M3.5 7L6 9.5L10.5 4.5" stroke="#fff" stroke-width="1.8" fill="none"/></svg>Create all your reports online with simple drag &amp; drop</li>
    <li><svg width="14" height="14" viewBox="0 0 14 14"><circle cx="7" cy="7" r="7" fill="#f05a22"/><path d="M3.5 7L6 9.5L10.5 4.5" stroke="#fff" stroke-width="1.8" fill="none"/></svg>Agile data abstraction layer turns data into Key Performance Indicators</li>
    <li><svg width="14" height="14" viewBox="0 0 14 14"><circle cx="7" cy="7" r="7" fill="#f05a22"/><path d="M3.5 7L6 9.5L10.5 4.5" stroke="#fff" stroke-width="1.8" fill="none"/></svg>Automated data gathering from all data sources</li>
  </ul>
  <div class="abs btn-ghost">REQUEST A DEMO</div>
</section>

<!-- contact -->
<section>
  <div class="abs contact"></div>
  <h2 class="abs section-title" style="top:2124px;color:var(--white);font-weight:300">CONTACT US</h2>
  <div class="abs field" style="left:186px;top:2190px;width:406px">FIRST NAME</div>
  <div class="abs field" style="left:610px;top:2190px;width:406px">LAST NAME</div>
  <div class="abs field" style="left:186px;top:2238px;width:406px">EMAIL</div>
  <div class="abs field" style="left:610px;top:2238px;width:406px">PHONE</div>
  <div class="abs field" style="left:186px;top:2288px;width:830px;height:64px">MESSAGE</div>
  <div class="abs btn-submit">SUBMIT</div>
</section>

<!-- map -->
<div class="abs map" role="img" aria-label="Street map of the city and surrounding area with the office location"></div>

<!-- footer -->
<footer>
  <div class="abs footer"></div>
  <h3 class="abs foot-head" style="left:110px">QUICK LINKS</h3>
  <ul class="abs foot-list" style="left:112px">
    <li><span class="bullet"></span>HOME</li>
    <li><span class="bullet"></span>ABOUT US</li>
    <li><span class="bullet"></span>SERVICES</li>
    <li><span class="bullet"></span>PROFILES</li>
    <li><span class="bullet"></span>TIPS &amp; LINKS</li>
    <li><span class="bullet"></span>CLIENT LOGIN</li>
    <li><span style="width:5px"></span>CONTACT</li>
  </ul>

  <h3 class="abs foot-head" style="left:325px">ADDRESS</h3>
  <ul class="abs foot-list" style="left:325px">
    <li class="contact-line orange-text"><svg width="12" height="16" viewBox="0 0 12 16"><path d="M6 0C2.7 0 0 2.6 0 5.8C0 10 6 16 6 16S12 10 12 5.8C12 2.6 9.3 0 6 0Z" fill="#f05a22"/><circle cx="6" cy="6" r="2.2" fill="#fff"/></svg>Lindvale / Nordmark</li>
    <li class="contact-line"><svg width="12" height="16" viewBox="0 0 12 16"><rect x="1.5" y="1" width="9" height="14" rx="1.5" fill="none" stroke="#666" stroke-width="1.4"/><circle cx="6" cy="12.5" r="1" fill="#666"/></svg>+44 7700 900418</li>
    <li class="contact-line"><svg width="14" height="10" viewBox="0 0 14 10"><rect x=".7" y=".7" width="12.6" height="8.6" fill="none" stroke="#666" stroke-width="1.4"/><path d="M.7 .7L7 6L13.3 .7" fill="none" stroke="#666" stroke-width="1.4"/></svg>hello@kestrelpartners.example</li>
    <li class="contact-line"><svg width="14" height="14" viewBox="0 0 14 14" fill="none" stroke="#666" stroke-width="1.3"><circle cx="7" cy="7" r="6"/><path d="M1 7H13M7 1C4 4 4 10 7 13M7 1C10 4 10 10 7 13"/></svg>www.kestrelpartners.example</li>
  </ul>

  <h3 class="abs foot-head" style="left:637px">FOLLOW US</h3>
  <ul class="abs foot-list" style="left:639px;top:2786px">
    <li style="height:26px"><span class="social-dot"></span>Chatter</li>
    <li style="height:26px"><span class="social-dot"></span>Facepage</li>
    <li style="height:26px"><span class="social-dot"></span>Mail</li>
    <li style="height:26px"><span class="social-dot"></span>Circle+</li>
  </ul>

  <div class="abs brand" style="left:816px;top:2748px">
    <span class="brand-dot"></span>
    <span class="brand-name">KESTREL PARTNERS</span>
  </div>
  <p class="abs foot-about">Deinde disputat, quod cuiusque generis animantium statui deceat extremum. Sed vobis voluptatum perceptarum recordatio vitam</p>
  <p class="abs copyright">Copyright © 2017 Kestrel Partners</p>
</footer>

</body>
</html>
```